Web Site Design For Real Estate Sales Project

The idea behind this project is pretty simple. I am putting my penthouse apartment up for sale and am trying to be creative in selling it.
Technically this will be pretty simple, it will be 3 pages but graphically this has to be as impressive as possible which is why I am trying Pixel Harbor.
The apartment is located in Barra Da Tijuca, Rio De Janeiro, Brazil. (This is where the 2016 Meridian Regatta will be held)
I am looking for an index page and 2 sub-pages. I am open to all kinds of designs and navigation's but it has to make an impression quickly with a professional and enticing design. The index page should make it obvious that there is a penthouse apartment for sale in Barra Da Tijuca ( suburb of Rio De Janeiro). The first sub page is about the Condominium where the apartment is located, the second sub page is about the apartment itself.
Here is a more detailed description of what the 3 pages should be about.
Index Page
This is the landing page and should make it obvious that there is an apartment for sale in Barra Da Tijuca, Rio De Janeiro with the following attributes
251 SQ M
Duplex Penthouse
4 suites
Price R$ 2.200.000
Price per SQ M: R$ 8.764
First Sub-Page
This is about the Condominium which is called "Gentle Palm Residences" with the following bullets
*Family friendly and safe
*Direct access to the beach
*Many amenities like pool, football court, gym, sauna
There should be some photos of the condominium and a link to the site of the condominium ( www.gprvx.com )
Second Sub-page
This is about the apartment. It should list in bullets the features of the apartment and then have a photo gallery of the view and various rooms. I have attached sample photos but will eventually have to use more photos.
Apartment Features
Price: R$ 2.220.000
251 m2 Duplex Penthouse
4 suites
maids room with bath
guest bathroom
living room
dinning room
Terrace with heated pool for year round use
Veranda
As mentioned above I am open to all designs and navigation so feel free to be creative. The important thing is catch peoples attention and get the message across in a few seconds, which is that there is an apartment for sale at this price with these features in this location. I will then use brightlist promoter and SEO to get people to the site.
Thanks
Target Market(s)
Men and Women from 30-60 years of age.
Industry/Entity Type
Apartment

```html
<!DOCTYPE html>
<html lang="en">
<head>
<meta charset="utf-8">
<title>Gentle Palm Residences</title>
<link href="https://fonts.googleapis.com/css2?family=Open+Sans:ital,wght@0,400;0,600;0,700;1,600;1,700&display=swap" rel="stylesheet">
<style>
:root{
  --blue:#0c7fbf;
  --charcoal:#474747;
  --page:#f3f3f3;
  --panel:#fafafa;
  --footer:#e4e4e4;
  --text:#555;
  --heading:#333;
  --white:#fff;
}
*{margin:0;padding:0;box-sizing:border-box}
html,body{width:1165px;height:1200px;overflow:hidden}
body{font-family:"Open Sans",Arial,sans-serif;color:var(--text);position:relative}
.city-backdrop{position:absolute;inset:0;background:linear-gradient(90deg,#8c949c 0%,#b4b8ba 20%,#c2c0b8 50%,#a8aaa8 80%,#8a9096 100%)}
.city-backdrop::after{content:"";position:absolute;inset:0;background:linear-gradient(180deg,rgba(180,190,200,.4),rgba(120,130,110,.35))}
.page-top{position:absolute;left:57px;top:0;width:928px;height:694px;background:var(--page)}
.page-bottom{position:absolute;left:57px;top:794px;width:928px;height:406px;background:var(--page)}
.brand{position:absolute;left:82px;top:42px;width:140px;font-size:22px;font-weight:600;color:var(--blue);line-height:1.15}
.phone{position:absolute;right:216px;top:18px;display:flex;align-items:center;gap:10px;font-size:16px;font-weight:700;font-style:italic;color:var(--blue)}
.social{position:absolute;left:780px;top:54px}
.nav{position:absolute;left:57px;top:130px;width:928px;height:72px;background:var(--white);display:flex;align-items:center;padding-left:19px}
.nav a{font-size:17px;color:#555;text-decoration:none;padding:0 24px;position:relative;line-height:37px}
.nav a+a::before{content:"";position:absolute;left:-4px;top:-2px;width:10px;height:42px;background:linear-gradient(90deg,#e6e6e6,rgba(255,255,255,0))}
.nav a.active{background:var(--blue);color:var(--white);padding:0 13px;margin-right:14px}
.search{position:absolute;right:0;top:0;width:31px;height:72px;background:var(--blue);display:flex;align-items:center;justify-content:center}
.slider{position:absolute;left:70px;top:218px;width:901px;height:476px;border:3px solid var(--white);box-shadow:0 0 4px rgba(0,0,0,.25);background:linear-gradient(180deg,#c9cfd2 0%,#a6a59d 35%,#7d6d62 60%,#cdc9c2 80%,#9c9690 100%)}
.arrow{position:absolute;top:178px;width:80px;height:80px;border-radius:50%;border:1px solid rgba(255,255,255,.8)}
.arrow.prev{left:13px}.arrow.next{right:13px}
.arrow svg{position:absolute;inset:0;margin:auto}
.cards{position:absolute;left:86px;top:586px;display:flex;gap:23px}
.card{width:274px}
.card-photo{height:212px;border:1px solid var(--white)}
.card-body{height:101px;padding:6px 12px;color:var(--white);position:relative}
.card-body h3{font-size:18px;font-weight:600;margin-bottom:4px}
.card-body p{font-size:13px;line-height:18px}
.card-body .more{position:absolute;right:16px;bottom:8px;font-size:13px}
.card.dark .card-body{background:var(--charcoal)}
.card.blue .card-body{background:var(--blue)}
.card.blue .more{color:#111}
.welcome{position:absolute;left:70px;top:922px;width:901px;height:154px;background:var(--panel);border:1px solid #ddd;padding:18px 19px}
.welcome h2{font-size:18px;font-weight:600;color:var(--heading);margin-bottom:10px}
.welcome p{font-size:13px;line-height:22px;width:760px;color:#666}
.welcome strong{font-weight:600;color:#444}
.btn{position:absolute;right:15px;bottom:16px;background:var(--blue);color:var(--white);font-size:14px;font-weight:600;padding:6px 14px;border-radius:16px}
.welcome::after{content:"";position:absolute;left:20px;right:20px;bottom:-10px;height:10px;background:radial-gradient(ellipse at top,rgba(12,127,191,.35),rgba(12,127,191,0) 70%)}
.footer{position:absolute;left:57px;top:1113px;width:928px;height:87px;background:var(--footer);display:flex;align-items:center;justify-content:space-between;padding:0 15px 0 17px;font-size:14px}
.crumbs a{color:var(--blue);text-decoration:none}
.crumbs span{color:#333}
.footer-brand{font-size:14px;font-weight:600;color:#333;width:90px;text-align:center;line-height:1.1;margin-left:60px}
.copyright{font-size:13px;color:#555}
</style>
</head>
<body>
<div class="city-backdrop" role="img" aria-label="Aerial view of beachfront high-rise towers"></div>
<div class="page-top"></div>
<div class="page-bottom"></div>

<div class="brand">Gentle Palm Residences</div>

<div class="phone">
  <svg width="24" height="26" viewBox="0 0 24 26"><path d="M5 4h6l-1 6-3 1c1 3 3 5 6 6l1-3 6-1v6c0 2-2 3-4 3C8 21 2 15 2 7c0-2 1-3 3-3z" fill="#0c7fbf"/></svg>
  555.014.2280
</div>
<svg class="social" width="182" height="40" viewBox="0 0 182 40">
  <g fill="#0c7fbf">
    <polygon points="20,1 25,13 38,14 28,22 31,36 20,29 9,36 12,22 2,14 15,13"/>
    <polygon transform="translate(45 0)" points="20,1 25,13 38,14 28,22 31,36 20,29 9,36 12,22 2,14 15,13"/>
    <polygon transform="translate(90 0)" points="20,1 25,13 38,14 28,22 31,36 20,29 9,36 12,22 2,14 15,13"/>
    <polygon transform="translate(135 0)" points="20,1 25,13 38,14 28,22 31,36 20,29 9,36 12,22 2,14 15,13"/>
  </g>
</svg>

<nav class="nav">
  <a class="active">Home</a>
  <a>Barra Da Tijuca</a>
  <a>Rio De Janeiro</a>
  <a>Brazil</a>
  <a>Contact Us</a>
  <div class="search"><svg width="16" height="16" viewBox="0 0 16 16"><circle cx="9.5" cy="6.5" r="4.5" fill="none" stroke="#fff" stroke-width="2"/><line x1="6" y1="10" x2="2" y2="14" stroke="#fff" stroke-width="2.5"/></svg></div>
</nav>

<div class="slider" role="img" aria-label="Penthouse rooftop terrace with pool and mountain view">
  <div class="arrow prev"><svg width="28" height="48" viewBox="0 0 28 48"><polyline points="22,4 6,24 22,44" fill="none" stroke="#fff" stroke-width="6"/></svg></div>
  <div class="arrow next"><svg width="28" height="48" viewBox="0 0 28 48"><polyline points="6,4 22,24 6,44" fill="none" stroke="#fff" stroke-width="6"/></svg></div>
</div>

<div class="cards">
  <div class="card dark">
    <div class="card-photo" role="img" aria-label="Beachfront towers along the coast" style="background:linear-gradient(180deg,#b8c4cc,#8e9294 55%,#c8c0ac)"></div>
    <div class="card-body"><h3>Barra Da Tijuca</h3><p>Duplex penthouse for sale: 251 sq m, 4 suites, heated pool.</p><span class="more">Read more</span></div>
  </div>
  <div class="card blue">
    <div class="card-photo" role="img" aria-label="Condominium entrance gate" style="background:linear-gradient(180deg,#b4b6b0,#7e806e 55%,#5e6450)"></div>
    <div class="card-body"><h3>Rio De Janeiro</h3><p>Price R$ 2.200.000 &ndash; only R$ 8.764 per sq m.</p><span class="more">Read more</span></div>
  </div>
  <div class="card blue">
    <div class="card-photo" role="img" aria-label="Apartment living room interior" style="background:linear-gradient(180deg,#c6c2bc,#6e5a52 55%,#5a2c22)"></div>
    <div class="card-body"><h3>Brazil</h3><p>Host city of the 2016 Meridian Regatta, by the beach.</p><span class="more">Read more</span></div>
  </div>
</div>

<section class="welcome">
  <h2>Wel come to our site</h2>
  <p><strong>Duplex penthouse for sale in Barra Da Tijuca, Rio De Janeiro.</strong> 251 sq m with 4 suites, maids room with bath, guest bathroom, living and dining rooms, veranda and a terrace with heated pool for year round use. <strong>Price R$ 2.200.000</strong> (R$ 8.764 per sq m). Set in Gentle Palm Residences: family friendly and safe, direct access to the beach, pool, football court, gym and sauna.</p>
  <span class="btn">Read more</span>
</section>

<footer class="footer">
  <div class="crumbs"><a>Barra Da Tijuca</a> <span>&nbsp;/&nbsp; Rio De Janeiro &nbsp;/&nbsp; Brazil</span></div>
  <div class="footer-brand">Gentle Palm Residences</div>
  <div class="copyright">Copyright 2013&nbsp; Gentle Palm Residences. All Right Reseved</div>
</footer>
</body>
</html>
```